Unique Hair Product needs upscale Tube Design

Miravel's Lustre is a hair product company. I need a tube design for a 4oz ABL (soft aluminum) tube which incorporates my logo and product information and usage. The product is a high-end treatment for thicker, darker hair.

Miravel's Lustre is a unique, strengthening color treatment, that will thicken weak, damaged hair, while enhancing hair color naturally, with henna.

Target Market(s)

Women age 17 and up

Industry/Entity Type

Hair Care Product

Requirements
Must have
• "Strengthening, Color enhancing, Hair treatment" this product description must be on the front of the tube. Please use diagram below.
• Must have logo placed strategically, and placed beautifully. I need the tube design to be elegant and beautiful because it is a high end product. Please use colors that you think would look nice and appeal to women. I was thinking a nice light olive green, with a white logo, but play with it until it looks really pretty.
• It will be going into a box, similar to the one below.
Nice to have
• Elegance, clarity and sharp
• please use the diagram to properly place the design in the designated space below
Should not have
• Please no cursive writing

```html
<!DOCTYPE html>
<html lang="en">
<head>
<meta charset="utf-8">
<title>Miravel's Lustre – Tube Label</title>
<link rel="stylesheet" href="https://fonts.googleapis.com/css2?family=Raleway:wght@300;400&family=Oswald:wght@500&family=Cinzel:wght@400&display=swap">
<style>
  :root {
    --page: #ffffff;
    --panel-light: #f3f3f3;
    --panel-dark: #3a3732;
    --ink-dark: #3a3732;
    --ink-light: #f4f2ee;
  }
  html, body {
    margin: 0;
    padding: 0;
    width: 1200px;
    height: 1000px;
    overflow: hidden;
    background: var(--page);
  }
  .canvas {
    position: relative;
    width: 1200px;
    height: 1000px;
  }
  .label {
    position: absolute;
    left: 282px;
    top: 141px;
    width: 636px;
    height: 719px;
  }

  /* Front panel */
  .front {
    position: absolute;
    left: 0;
    top: 0;
    width: 318px;
    height: 719px;
    background: var(--panel-light);
    color: var(--ink-dark);
    text-align: center;
    font-family: "Raleway", sans-serif;
  }
  .front__intro {
    position: absolute;
    top: 33px;
    left: 0;
    width: 100%;
    margin: 0;
    font-size: 19px;
    font-weight: 400;
  }
  .front__brand-band {
    position: absolute;
    top: 79px;
    left: 0;
    width: 100%;
    height: 148px;
    background: var(--panel-dark);
    display: flex;
    align-items: center;
    justify-content: center;
    gap: 12px;
  }
  .brand-dot {
    width: 14px;
    height: 14px;
    border-radius: 50%;
    background: var(--ink-light);
  }
  .brand-name {
    font-family: "Raleway", sans-serif;
    font-weight: 400;
    color: var(--ink-light);
    letter-spacing: 1px;
  }
  .front__brand-band .brand-name { font-size: 26px; }

  .front__copy {
    position: absolute;
    top: 248px;
    left: 0;
    width: 100%;
  }
  .copy-line {
    margin: 0;
    font-size: 19px;
    line-height: 30px;
    font-weight: 400;
  }
  .claim {
    margin: 0;
    font-family: "Oswald", sans-serif;
    font-weight: 500;
    font-size: 46px;
    line-height: 78px;
    letter-spacing: 0.3px;
  }
  .front__net-band {
    position: absolute;
    left: 0;
    bottom: 0;
    width: 100%;
    height: 36px;
    background: var(--panel-dark);
    color: #c9c6c0;
    font-size: 19px;
    font-weight: 300;
    line-height: 38px;
  }

  /* Back panel */
  .back {
    position: absolute;
    left: 318px;
    top: 0;
    width: 318px;
    height: 719px;
    background: var(--panel-dark);
    color: var(--ink-light);
  }
  .back__brand {
    position: absolute;
    top: 96px;
    left: 0;
    width: 100%;
    display: flex;
    align-items: center;
    justify-content: center;
    gap: 8px;
  }
  .back__brand .brand-dot { width: 10px; height: 10px; }
  .back__brand .brand-name { font-size: 17px; }
  .back__title {
    position: absolute;
    top: 176px;
    left: 0;
    width: 100%;
    margin: 0;
    text-align: center;
    font-family: "Cinzel", serif;
    font-weight: 400;
    font-size: 20px;
    line-height: 25px;
    letter-spacing: 2px;
  }
  .ingredients {
    position: absolute;
    top: 298px;
    left: 30px;
    margin: 0;
    padding: 0;
    list-style: none;
    font-family: "Raleway", sans-serif;
    font-size: 14px;
    line-height: 27px;
  }
</style>
</head>
<body>
<div class="canvas">
  <div class="label">
    <section class="front">
      <p class="front__intro">Miravel's Lustre is a unique,</p>
      <div class="front__brand-band">
        <span class="brand-dot"></span>
        <span class="brand-name">Miravel's Lustre</span>
      </div>
      <div class="front__copy">
        <p class="copy-line">strengthening color treatment,</p>
        <p class="claim">Strengthening,</p>
        <p class="copy-line">that will thicken weak,</p>
        <p class="claim">Color Enhancing,</p>
        <p class="copy-line">damaged hair,<br>while enhancing hair</p>
        <p class="claim">Hair Treatment</p>
        <p class="copy-line">color naturally,<br>with henna.</p>
      </div>
      <div class="front__net-band">Netto 120g</div>
    </section>

    <section class="back">
      <div class="back__brand">
        <span class="brand-dot"></span>
        <span class="brand-name">Miravel's Lustre</span>
      </div>
      <h1 class="back__title">Strengthening<br>Color Enhancing<br>Hair Treatment</h1>
      <ul class="ingredients">
        <li>Ingredients:</li>
        <li>Lorem ipsum dolor sit amet,</li>
        <li>consectetuer adipiscing elit.</li>
        <li>In rutrum. Integer in sapien.</li>
        <li>Fusce dui leo, imperdiet in,</li>
        <li>aliquam sit amet, feugiat eu, orci.</li>
        <li>Nullam eget nisl. Aliquam erat volutpat.</li>
        <li>Proin pede metus, vulputate nec,</li>
        <li>fermentum fringilla, vehicula vitae,</li>
        <li>justo. Vivamus ac leo pretium faucibus.</li>
        <li>Nullam rhoncus aliquam metus.</li>
        <li>Proin mattis lacinia justo.</li>
        <li>Nullam rhoncus aliquam metus.</li>
        <li>Proin mattis lacinia justo.</li>
      </ul>
    </section>
  </div>
</div>
</body>
</html>
```